Business Card Design and a letter head logo

50/50 share milker dairy farmer of 400 cows with a silage and haymaking sideline business
15 years farming currently looking for new opportunities within the dairy farming sector. trying to put together a portfolio to get another 50/50 share milking job aswell

Industry/Entity Type

Farming

Contact Information for Business Card

Birch Farming LTD
Corwin & Felicity Hartley
382 Kelvale Ridge Highway
RD1 Tawhiro 0184
Whangarei
hartley.corwin@lumenmail.co.nz
0273948261
(09) 4715293

```html
<!DOCTYPE html>
<html lang="en">
<head>
<meta charset="utf-8">
<title>Birch Farming LTD – Business Card</title>
<link rel="stylesheet" href="https://fonts.googleapis.com/css2?family=Lato:wght@400;700&display=swap">
<style>
  :root {
    --backdrop: #3b332e;
    --card: #0e0e0e;
    --card-edge: #1c1c1c;
    --green: #4fb043;
    --rust: #b4562b;
    --silver: #c4c4c4;
  }
  * { margin: 0; padding: 0; box-sizing: border-box; }
  html, body {
    width: 1200px;
    height: 844px;
    overflow: hidden;
    background: var(--backdrop);
    font-family: "Lato", sans-serif;
  }
  .stage {
    position: relative;
    width: 1200px;
    height: 844px;
  }
  .card {
    position: absolute;
    top: 273px;
    width: 520px;
    height: 298px;
    background: var(--card);
    border: 1px solid var(--card-edge);
    border-radius: 4px;
    box-shadow: 0 14px 30px rgba(0, 0, 0, 0.45);
  }
  .card--front { left: 60px; }
  .card--back { left: 620px; }

  .brand {
    position: absolute;
    display: flex;
    flex-direction: column;
    align-items: center;
    gap: 14px;
  }
  .brand__dot {
    width: 44px;
    height: 44px;
    border-radius: 50%;
  }
  .brand__name {
    font-weight: 700;
    font-size: 24px;
    letter-spacing: 0.5px;
    white-space: nowrap;
  }

  .card--front .brand { left: 0; width: 260px; top: 110px; }
  .card--front .brand__dot { background: var(--green); }
  .card--front .brand__name { color: var(--green); }

  .card--back .brand { left: 0; width: 100%; top: 86px; }
  .card--back .brand__dot { background: var(--silver); width: 52px; height: 52px; }
  .card--back .brand__name { color: var(--silver); font-size: 32px; }

  .contact {
    position: absolute;
    left: 272px;
    top: 62px;
    color: var(--rust);
    font-size: 13.5px;
    line-height: 1.3;
    white-space: nowrap;
  }
  .contact__name {
    color: var(--green);
    font-size: 20px;
    font-weight: 400;
    line-height: 1.1;
  }
  .contact__role { margin-bottom: 16px; }
  .contact__address { margin-bottom: 16px; }
  .contact__label { color: var(--green); }
</style>
</head>
<body>
<main class="stage">
  <section class="card card--front">
    <div class="brand">
      <span class="brand__dot"></span>
      <span class="brand__name">Birch Farming LTD</span>
    </div>
    <div class="contact">
      <p class="contact__name">Marcus Ellery</p>
      <p class="contact__role">Operations Director</p>
      <p class="contact__address">4821, Harlow Field Road<br>Kelvale Downs, 503217.</p>
      <p><span class="contact__label">T:</span> 044-627 318 905</p>
      <p><span class="contact__label">E:</span> info@fieldpost.com</p>
      <p><span class="contact__label">W:</span> www.fieldpage.com</p>
    </div>
  </section>

  <section class="card card--back">
    <div class="brand">
      <span class="brand__dot"></span>
      <span class="brand__name">Birch Farming LTD</span>
    </div>
  </section>
</main>
</body>
</html>
```